Restaurant Digital TV Menu Pictures

Need a digital menu board, image square of food. Something simple for customer to look and point to or say the food number. Image square 4x6, 5x7 or various of that. Vietnamese restaurant type food. I need template created and designer choice of design. Color scheme orange and white and little green. I would like to in the title of the food myself and written detail myself. I just need the template and possible have the design edit the picture a bit. Total food about 30 image will mostly be about 20-30 images. This will be display on a TV screen 16:9 size on a 55 inch tv. Attached is the food menu item. Also attach how the image off food will be taken. Also attach of other people design on the web. However, I would like number be label on the food item. I can find tune the correct information and food type and numbers later.

Font styles to use
Decorative

Colors
f37122
fffefb
9bcb3c

Requirements
Must have
• Photo edit food image basic making it pop. Make it look better, not magic, but better than my photography. Asian feel to the design.
Nice to have
• Fresh image of ingredients, (cilantro, freshly cook, non fast food) Image of green food

```html
<!DOCTYPE html>
<html lang="en">
<head>
<meta charset="utf-8">
<title>Info Board – Menu Tiles</title>
<link rel="stylesheet" href="https://fonts.googleapis.com/css2?family=Oswald:wght@500;600;700&family=Roboto:wght@400;500&display=swap">
<style>
  :root{
    --orange:#f37122;
    --green:#9bcb3c;
    --cream:#fffefb;
    --ink:#1d1d1d;
    --stage:#202020;
    --copy:#333;
  }
  *{box-sizing:border-box;margin:0;padding:0}
  html,body{width:1200px;height:835px;overflow:hidden}
  body{background:radial-gradient(ellipse at 40% 40%,#2b2b2b 0%,var(--stage) 70%,#171717 100%);position:relative;font-family:'Roboto',sans-serif}

  .tile-grid{position:absolute;left:19px;top:18px;display:grid;grid-template-columns:repeat(5,185px);grid-template-rows:repeat(4,184px);column-gap:11px;row-gap:17px}

  .menu-tile{position:relative;width:185px;height:184px;background:var(--cream);overflow:hidden;box-shadow:0 2px 6px rgba(0,0,0,.5)}
  .menu-tile::before{content:"";position:absolute;left:60px;top:40px;width:130px;height:140px;background-image:radial-gradient(#d9d9d9 0.8px,transparent 1px);background-size:4px 4px;opacity:.7}

  .tile-frame{position:absolute;left:97px;top:50px;width:106px;height:106px;border:3px solid var(--orange);transform:rotate(45deg)}
  .tile-photo{position:absolute;left:105px;top:40px;width:112px;height:112px;transform:rotate(45deg);transform-origin:center}
  .tile-photo span{display:block;width:100%;height:100%}

  .tile-title{position:absolute;left:5px;top:3px;font-family:'Oswald',sans-serif;font-weight:600;line-height:29px;font-size:29px;letter-spacing:.2px;z-index:2}
  .tile-title .lead{color:var(--orange);display:block}
  .tile-title .menu-word{color:var(--green);display:block}
  .tile-title.narrow{font-size:24px;line-height:25px}
  .tile-title.narrow .menu-word{font-size:26px}

  .rule-green{position:absolute;left:6px;top:46px;width:2px;height:124px;background:var(--green)}
  .rule-orange{position:absolute;left:11px;top:110px;width:2px;height:32px;background:var(--orange)}

  .tile-copy{position:absolute;left:19px;top:89px;width:82px;font-size:5.4px;line-height:7px;color:var(--copy)}

  .deal-badge{position:absolute;left:121px;top:125px;width:42px;height:42px;background:var(--ink);border:3px solid var(--green);transform:rotate(45deg);z-index:3}
  .deal-text{position:absolute;left:121px;top:131px;width:42px;text-align:center;font-family:'Oswald',sans-serif;color:var(--green);z-index:4;line-height:1}
  .deal-text b{display:block;font-size:16px;font-weight:500}
  .deal-text small{display:block;font-size:10px;font-weight:500;margin-top:-1px}

  .order-bar{position:absolute;left:0;top:162px;width:92px;height:14px;background:var(--ink);clip-path:polygon(0 0,100% 0,92% 100%,0 100%);display:flex;align-items:center;padding-left:5px;gap:5px;z-index:2}
  .order-bar svg{width:11px;height:11px;flex:none}
  .order-bar span{color:#fff;font-size:8.6px;font-weight:500;letter-spacing:.2px}

  .base-stripe{position:absolute;left:0;bottom:0;width:10px;height:5px;background:linear-gradient(90deg,var(--orange) 0 40%,var(--green) 40% 70%,var(--orange) 70%)}

  /* photo tones per dish */
  .photo-chicken{background:radial-gradient(circle at 55% 45%,#c98a45 0%,#a8652c 45%,#e9e3dc 90%)}
  .photo-rice{background:radial-gradient(circle at 45% 55%,#f1d27a 0%,#b5622e 40%,#7d3a22 70%,#e7b561 100%)}
  .photo-veg{background:radial-gradient(circle at 50% 50%,#c48643 0%,#9b5f2c 50%,#d8d2c8 95%)}
  .photo-beef{background:radial-gradient(circle at 55% 55%,#5b3a27 0%,#3c2417 40%,#8b5a8f 70%,#1a1a1a 95%)}

  .info-panel{position:absolute;left:996px;top:19px;width:181px;height:787px;background:var(--cream);border:3px solid var(--orange);font-family:'Oswald',sans-serif;font-weight:700;color:#2a2a2a;text-align:center}
  .info-panel .info-word{font-size:70px;line-height:1;margin-top:22px;letter-spacing:1px}
  .info-panel .board-letters{display:flex;flex-direction:column;align-items:center;margin-top:-2px}
  .info-panel .board-letters span{font-size:124px;line-height:126px;display:block;transform:scaleX(.85)}
</style>
</head>
<body>

<main class="tile-grid">
  <!-- row 1 -->
  <article class="menu-tile"><div class="tile-frame"></div><div class="tile-photo"><span class="photo-chicken" role="img" aria-label="Photo of crispy fried chicken with cilantro"></span></div><h2 class="tile-title"><span class="lead">SPECIAL</span><span class="menu-word">MENU</span></h2><i class="rule-green"></i><i class="rule-orange"></i><p class="tile-copy">Lorem ipsum dolor sit amet, consectetur adipiscing elit, sed do eiusmod tempor incididunt ut labore et dolore magna aliqua. Ut enim ad minim veniam, quis ostrud itation ullamco</p><div class="deal-badge"></div><div class="deal-text"><b>50%</b><small>OFF</small></div><div class="order-bar"><svg viewBox="0 0 12 12"><circle cx="6" cy="6" r="5.5" fill="#fff"/><path d="M4 3.2l1.1 1.5-.7.8c.5 1 1.2 1.7 2.1 2.1l.8-.7 1.5 1.1-.6 1c-2.6-.4-4.5-2.4-4.9-5z" fill="#1d1d1d"/></svg><span>ORDER NOW</span></div><i class="base-stripe"></i></article>
  <article class="menu-tile"><div class="tile-frame"></div><div class="tile-photo"><span class="photo-rice" role="img" aria-label="Photo of fried rice plate with egg and spring roll"></span></div><h2 class="tile-title narrow"><span class="lead">ADDITIONAL</span><span class="menu-word">MENU</span></h2><i class="rule-green"></i><p class="tile-copy">Lorem ipsum dolor sit amet, consectetur adipiscing elit, sed do eiusmod tempor incididunt ut labore et dolore magna aliqua. Ut enim ad minim veniam, quis ostrud itation ullamco</p><div class="deal-badge"></div><div class="deal-text"><b>50%</b><small>OFF</small></div><div class="order-bar"><svg viewBox="0 0 12 12"><circle cx="6" cy="6" r="5.5" fill="#fff"/><path d="M4 3.2l1.1 1.5-.7.8c.5 1 1.2 1.7 2.1 2.1l.8-.7 1.5 1.1-.6 1c-2.6-.4-4.5-2.4-4.9-5z" fill="#1d1d1d"/></svg><span>ORDER NOW</span></div><i class="base-stripe"></i></article>
  <article class="menu-tile"><div class="tile-frame"></div><div class="tile-photo"><span class="photo-veg" role="img" aria-label="Photo of crispy fried dish with cilantro"></span></div><h2 class="tile-title narrow"><span class="lead">VEGETERIAN</span><span class="menu-word">MENU</span></h2><i class="rule-green"></i><p class="tile-copy">Lorem ipsum dolor sit amet, consectetur adipiscing elit, sed do eiusmod tempor incididunt ut labore et dolore magna aliqua. Ut enim ad minim veniam, quis ostrud itation ullamco</p><div class="deal-badge"></div><div class="deal-text"><b>50%</b><small>OFF</small></div><div class="order-bar"><svg viewBox="0 0 12 12"><circle cx="6" cy="6" r="5.5" fill="#fff"/><path d="M4 3.2l1.1 1.5-.7.8c.5 1 1.2 1.7 2.1 2.1l.8-.7 1.5 1.1-.6 1c-2.6-.4-4.5-2.4-4.9-5z" fill="#1d1d1d"/></svg><span>ORDER NOW</span></div><i class="base-stripe"></i></article>
  <article class="menu-tile"><div class="tile-frame"></div><div class="tile-photo"><span class="photo-beef" role="img" aria-label="Photo of grilled beef bowl with slaw and dipping sauce"></span></div><h2 class="tile-title"><span class="lead">SPECIAL</span><span class="menu-word">MENU</span></h2><i class="rule-green"></i><p class="tile-copy">Lorem ipsum dolor sit amet, consectetur adipiscing elit, sed do eiusmod tempor incididunt ut labore et dolore magna aliqua. Ut enim ad minim veniam, quis ostrud itation ullamco</p><div class="deal-badge"></div><div class="deal-text"><b>50%</b><small>OFF</small></div><div class="order-bar"><svg viewBox="0 0 12 12"><circle cx="6" cy="6" r="5.5" fill="#fff"/><path d="M4 3.2l1.1 1.5-.7.8c.5 1 1.2 1.7 2.1 2.1l.8-.7 1.5 1.1-.6 1c-2.6-.4-4.5-2.4-4.9-5z" fill="#1d1d1d"/></svg><span>ORDER NOW</span></div><i class="base-stripe"></i></article>
  <article class="menu-tile"><div class="tile-frame"></div><div class="tile-photo"><span class="photo-beef" role="img" aria-label="Photo of grilled beef bowl with slaw and dipping sauce"></span></div><h2 class="tile-title"><span class="lead">TODAY'S</span><span class="menu-word">MENU</span></h2><i class="rule-green"></i><p class="tile-copy">Lorem ipsum dolor sit amet, consectetur adipiscing elit, sed do eiusmod tempor incididunt ut labore et dolore magna aliqua. Ut enim ad minim veniam, quis ostrud itation ullamco</p><div class="deal-badge"></div><div class="deal-text"><b>50%</b><small>OFF</small></div><div class="order-bar"><svg viewBox="0 0 12 12"><circle cx="6" cy="6" r="5.5" fill="#fff"/><path d="M4 3.2l1.1 1.5-.7.8c.5 1 1.2 1.7 2.1 2.1l.8-.7 1.5 1.1-.6 1c-2.6-.4-4.5-2.4-4.9-5z" fill="#1d1d1d"/></svg><span>ORDER NOW</span></div><i class="base-stripe"></i></article>

  <!-- row 2 -->
  <article class="menu-tile"><div class="tile-frame"></div><div class="tile-photo"><span class="photo-chicken" role="img" aria-label="Photo of crispy fried chicken with cilantro"></span></div><h2 class="tile-title"><span class="lead">SPECIAL</span><span class="menu-word">MENU</span></h2><i class="rule-green"></i><i class="rule-orange"></i><p class="tile-copy">Lorem ipsum dolor sit amet, consectetur adipiscing elit, sed do eiusmod tempor incididunt ut labore et dolore magna aliqua. Ut enim ad minim veniam, quis ostrud itation ullamco</p><div class="deal-badge"></div><div class="deal-text"><b>50%</b><small>OFF</small></div><div class="order-bar"><svg viewBox="0 0 12 12"><circle cx="6" cy="6" r="5.5" fill="#fff"/><path d="M4 3.2l1.1 1.5-.7.8c.5 1 1.2 1.7 2.1 2.1l.8-.7 1.5 1.1-.6 1c-2.6-.4-4.5-2.4-4.9-5z" fill="#1d1d1d"/></svg><span>ORDER NOW</span></div><i class="base-stripe"></i></article>
  <article class="menu-tile"><div class="tile-frame"></div><div class="tile-photo"><span class="photo-rice" role="img" aria-label="Photo of fried rice plate with egg and spring roll"></span></div><h2 class="tile-title narrow"><span class="lead">ADDITIONAL</span><span class="menu-word">MENU</span></h2><i class="rule-green"></i><p class="tile-copy">Lorem ipsum dolor sit amet, consectetur adipiscing elit, sed do eiusmod tempor incididunt ut labore et dolore magna aliqua. Ut enim ad minim veniam, quis ostrud itation ullamco</p><div class="deal-badge"></div><div class="deal-text"><b>50%</b><small>OFF</small></div><div class="order-bar"><svg viewBox="0 0 12 12"><circle cx="6" cy="6" r="5.5" fill="#fff"/><path d="M4 3.2l1.1 1.5-.7.8c.5 1 1.2 1.7 2.1 2.1l.8-.7 1.5 1.1-.6 1c-2.6-.4-4.5-2.4-4.9-5z" fill="#1d1d1d"/></svg><span>ORDER NOW</span></div><i class="base-stripe"></i></article>
  <article class="menu-tile"><div class="tile-frame"></div><div class="tile-photo"><span class="photo-veg" role="img" aria-label="Photo of crispy fried dish with cilantro"></span></div><h2 class="tile-title narrow"><span class="lead">VEGETERIAN</span><span class="menu-word">MENU</span></h2><i class="rule-green"></i><p class="tile-copy">Lorem ipsum dolor sit amet, consectetur adipiscing elit, sed do eiusmod tempor incididunt ut labore et dolore magna aliqua. Ut enim ad minim veniam, quis ostrud itation ullamco</p><div class="deal-badge"></div><div class="deal-text"><b>50%</b><small>OFF</small></div><div class="order-bar"><svg viewBox="0 0 12 12"><circle cx="6" cy="6" r="5.5" fill="#fff"/><path d="M4 3.2l1.1 1.5-.7.8c.5 1 1.2 1.7 2.1 2.1l.8-.7 1.5 1.1-.6 1c-2.6-.4-4.5-2.4-4.9-5z" fill="#1d1d1d"/></svg><span>ORDER NOW</span></div><i class="base-stripe"></i></article>
  <article class="menu-tile"><div class="tile-frame"></div><div class="tile-photo"><span class="photo-beef" role="img" aria-label="Photo of grilled beef bowl with slaw and dipping sauce"></span></div><h2 class="tile-title"><span class="lead">SPECIAL</span><span class="menu-word">MENU</span></h2><i class="rule-green"></i><p class="tile-copy">Lorem ipsum dolor sit amet, consectetur adipiscing elit, sed do eiusmod tempor incididunt ut labore et dolore magna aliqua. Ut enim ad minim veniam, quis ostrud itation ullamco</p><div class="deal-badge"></div><div class="deal-text"><b>50%</b><small>OFF</small></div><div class="order-bar"><svg viewBox="0 0 12 12"><circle cx="6" cy="6" r="5.5" fill="#fff"/><path d="M4 3.2l1.1 1.5-.7.8c.5 1 1.2 1.7 2.1 2.1l.8-.7 1.5 1.1-.6 1c-2.6-.4-4.5-2.4-4.9-5z" fill="#1d1d1d"/></svg><span>ORDER NOW</span></div><i class="base-stripe"></i></article>
  <article class="menu-tile"><div class="tile-frame"></div><div class="tile-photo"><span class="photo-beef" role="img" aria-label="Photo of grilled beef bowl with slaw and dipping sauce"></span></div><h2 class="tile-title"><span class="lead">TODAY'S</span><span class="menu-word">MENU</span></h2><i class="rule-green"></i><p class="tile-copy">Lorem ipsum dolor sit amet, consectetur adipiscing elit, sed do eiusmod tempor incididunt ut labore et dolore magna aliqua. Ut enim ad minim veniam, quis ostrud itation ullamco</p><div class="deal-badge"></div><div class="deal-text"><b>50%</b><small>OFF</small></div><div class="order-bar"><svg viewBox="0 0 12 12"><circle cx="6" cy="6" r="5.5" fill="#fff"/><path d="M4 3.2l1.1 1.5-.7.8c.5 1 1.2 1.7 2.1 2.1l.8-.7 1.5 1.1-.6 1c-2.6-.4-4.5-2.4-4.9-5z" fill="#1d1d1d"/></svg><span>ORDER NOW</span></div><i class="base-stripe"></i></article>

  <!-- row 3 -->
  <article class="menu-tile"><div class="tile-frame"></div><div class="tile-photo"><span class="photo-chicken" role="img" aria-label="Photo of crispy fried chicken with cilantro"></span></div><h2 class="tile-title"><span class="lead">SPECIAL</span><span class="menu-word">MENU</span></h2><i class="rule-green"></i><i class="rule-orange"></i><p class="tile-copy">Lorem ipsum dolor sit amet, consectetur adipiscing elit, sed do eiusmod tempor incididunt ut labore et dolore magna aliqua. Ut enim ad minim veniam, quis ostrud itation ullamco</p><div class="deal-badge"></div><div class="deal-text"><b>50%</b><small>OFF</small></div><div class="order-bar"><svg viewBox="0 0 12 12"><circle cx="6" cy="6" r="5.5" fill="#fff"/><path d="M4 3.2l1.1 1.5-.7.8c.5 1 1.2 1.7 2.1 2.1l.8-.7 1.5 1.1-.6 1c-2.6-.4-4.5-2.4-4.9-5z" fill="#1d1d1d"/></svg><span>ORDER NOW</span></div><i class="base-stripe"></i></article>
  <article class="menu-tile"><div class="tile-frame"></div><div class="tile-photo"><span class="photo-rice" role="img" aria-label="Photo of fried rice plate with egg and spring roll"></span></div><h2 class="tile-title narrow"><span class="lead">ADDITIONAL</span><span class="menu-word">MENU</span></h2><i class="rule-green"></i><p class="tile-copy">Lorem ipsum dolor sit amet, consectetur adipiscing elit, sed do eiusmod tempor incididunt ut labore et dolore magna aliqua. Ut enim ad minim veniam, quis ostrud itation ullamco</p><div class="deal-badge"></div><div class="deal-text"><b>50%</b><small>OFF</small></div><div class="order-bar"><svg viewBox="0 0 12 12"><circle cx="6" cy="6" r="5.5" fill="#fff"/><path d="M4 3.2l1.1 1.5-.7.8c.5 1 1.2 1.7 2.1 2.1l.8-.7 1.5 1.1-.6 1c-2.6-.4-4.5-2.4-4.9-5z" fill="#1d1d1d"/></svg><span>ORDER NOW</span></div><i class="base-stripe"></i></article>
  <article class="menu-tile"><div class="tile-frame"></div><div class="tile-photo"><span class="photo-veg" role="img" aria-label="Photo of crispy fried dish with cilantro"></span></div><h2 class="tile-title narrow"><span class="lead">VEGETERIAN</span><span class="menu-word">MENU</span></h2><i class="rule-green"></i><p class="tile-copy">Lorem ipsum dolor sit amet, consectetur adipiscing elit, sed do eiusmod tempor incididunt ut labore et dolore magna aliqua. Ut enim ad minim veniam, quis ostrud itation ullamco</p><div class="deal-badge"></div><div class="deal-text"><b>50%</b><small>OFF</small></div><div class="order-bar"><svg viewBox="0 0 12 12"><circle cx="6" cy="6" r="5.5" fill="#fff"/><path d="M4 3.2l1.1 1.5-.7.8c.5 1 1.2 1.7 2.1 2.1l.8-.7 1.5 1.1-.6 1c-2.6-.4-4.5-2.4-4.9-5z" fill="#1d1d1d"/></svg><span>ORDER NOW</span></div><i class="base-stripe"></i></article>
  <article class="menu-tile"><div class="tile-frame"></div><div class="tile-photo"><span class="photo-beef" role="img" aria-label="Photo of grilled beef bowl with slaw and dipping sauce"></span></div><h2 class="tile-title"><span class="lead">SPECIAL</span><span class="menu-word">MENU</span></h2><i class="rule-green"></i><p class="tile-copy">Lorem ipsum dolor sit amet, consectetur adipiscing elit, sed do eiusmod tempor incididunt ut labore et dolore magna aliqua. Ut enim ad minim veniam, quis ostrud itation ullamco</p><div class="deal-badge"></div><div class="deal-text"><b>50%</b><small>OFF</small></div><div class="order-bar"><svg viewBox="0 0 12 12"><circle cx="6" cy="6" r="5.5" fill="#fff"/><path d="M4 3.2l1.1 1.5-.7.8c.5 1 1.2 1.7 2.1 2.1l.8-.7 1.5 1.1-.6 1c-2.6-.4-4.5-2.4-4.9-5z" fill="#1d1d1d"/></svg><span>ORDER NOW</span></div><i class="base-stripe"></i></article>
  <article class="menu-tile"><div class="tile-frame"></div><div class="tile-photo"><span class="photo-beef" role="img" aria-label="Photo of grilled beef bowl with slaw and dipping sauce"></span></div><h2 class="tile-title"><span class="lead">TODAY'S</span><span class="menu-word">MENU</span></h2><i class="rule-green"></i><p class="tile-copy">Lorem ipsum dolor sit amet, consectetur adipiscing elit, sed do eiusmod tempor incididunt ut labore et dolore magna aliqua. Ut enim ad minim veniam, quis ostrud itation ullamco</p><div class="deal-badge"></div><div class="deal-text"><b>50%</b><small>OFF</small></div><div class="order-bar"><svg viewBox="0 0 12 12"><circle cx="6" cy="6" r="5.5" fill="#fff"/><path d="M4 3.2l1.1 1.5-.7.8c.5 1 1.2 1.7 2.1 2.1l.8-.7 1.5 1.1-.6 1c-2.6-.4-4.5-2.4-4.9-5z" fill="#1d1d1d"/></svg><span>ORDER NOW</span></div><i class="base-stripe"></i></article>

  <!-- row 4 -->
  <article class="menu-tile"><div class="tile-frame"></div><div class="tile-photo"><span class="photo-chicken" role="img" aria-label="Photo of crispy fried chicken with cilantro"></span></div><h2 class="tile-title"><span class="lead">SPECIAL</span><span class="menu-word">MENU</span></h2><i class="rule-green"></i><i class="rule-orange"></i><p class="tile-copy">Lorem ipsum dolor sit amet, consectetur adipiscing elit, sed do eiusmod tempor incididunt ut labore et dolore magna aliqua. Ut enim ad minim veniam, quis ostrud itation ullamco</p><div class="deal-badge"></div><div class="deal-text"><b>50%</b><small>OFF</small></div><div class="order-bar"><svg viewBox="0 0 12 12"><circle cx="6" cy="6" r="5.5" fill="#fff"/><path d="M4 3.2l1.1 1.5-.7.8c.5 1 1.2 1.7 2.1 2.1l.8-.7 1.5 1.1-.6 1c-2.6-.4-4.5-2.4-4.9-5z" fill="#1d1d1d"/></svg><span>ORDER NOW</span></div><i class="base-stripe"></i></article>
  <article class="menu-tile"><div class="tile-frame"></div><div class="tile-photo"><span class="photo-rice" role="img" aria-label="Photo of fried rice plate with egg and spring roll"></span></div><h2 class="tile-title narrow"><span class="lead">ADDITIONAL</span><span class="menu-word">MENU</span></h2><i class="rule-green"></i><p class="tile-copy">Lorem ipsum dolor sit amet, consectetur adipiscing elit, sed do eiusmod tempor incididunt ut labore et dolore magna aliqua. Ut enim ad minim veniam, quis ostrud itation ullamco</p><div class="deal-badge"></div><div class="deal-text"><b>50%</b><small>OFF</small></div><div class="order-bar"><svg viewBox="0 0 12 12"><circle cx="6" cy="6" r="5.5" fill="#fff"/><path d="M4 3.2l1.1 1.5-.7.8c.5 1 1.2 1.7 2.1 2.1l.8-.7 1.5 1.1-.6 1c-2.6-.4-4.5-2.4-4.9-5z" fill="#1d1d1d"/></svg><span>ORDER NOW</span></div><i class="base-stripe"></i></article>
  <article class="menu-tile"><div class="tile-frame"></div><div class="tile-photo"><span class="photo-veg" role="img" aria-label="Photo of crispy fried dish with cilantro"></span></div><h2 class="tile-title narrow"><span class="lead">VEGETERIAN</span><span class="menu-word">MENU</span></h2><i class="rule-green"></i><p class="tile-copy">Lorem ipsum dolor sit amet, consectetur adipiscing elit, sed do eiusmod tempor incididunt ut labore et dolore magna aliqua. Ut enim ad minim veniam, quis ostrud itation ullamco</p><div class="deal-badge"></div><div class="deal-text"><b>50%</b><small>OFF</small></div><div class="order-bar"><svg viewBox="0 0 12 12"><circle cx="6" cy="6" r="5.5" fill="#fff"/><path d="M4 3.2l1.1 1.5-.7.8c.5 1 1.2 1.7 2.1 2.1l.8-.7 1.5 1.1-.6 1c-2.6-.4-4.5-2.4-4.9-5z" fill="#1d1d1d"/></svg><span>ORDER NOW</span></div><i class="base-stripe"></i></article>
  <article class="menu-tile"><div class="tile-frame"></div><div class="tile-photo"><span class="photo-beef" role="img" aria-label="Photo of grilled beef bowl with slaw and dipping sauce"></span></div><h2 class="tile-title"><span class="lead">SPECIAL</span><span class="menu-word">MENU</span></h2><i class="rule-green"></i><p class="tile-copy">Lorem ipsum dolor sit amet, consectetur adipiscing elit, sed do eiusmod tempor incididunt ut labore et dolore magna aliqua. Ut enim ad minim veniam, quis ostrud itation ullamco</p><div class="deal-badge"></div><div class="deal-text"><b>50%</b><small>OFF</small></div><div class="order-bar"><svg viewBox="0 0 12 12"><circle cx="6" cy="6" r="5.5" fill="#fff"/><path d="M4 3.2l1.1 1.5-.7.8c.5 1 1.2 1.7 2.1 2.1l.8-.7 1.5 1.1-.6 1c-2.6-.4-4.5-2.4-4.9-5z" fill="#1d1d1d"/></svg><span>ORDER NOW</span></div><i class="base-stripe"></i></article>
  <article class="menu-tile"><div class="tile-frame"></div><div class="tile-photo"><span class="photo-beef" role="img" aria-label="Photo of grilled beef bowl with slaw and dipping sauce"></span></div><h2 class="tile-title"><span class="lead">TODAY'S</span><span class="menu-word">MENU</span></h2><i class="rule-green"></i><p class="tile-copy">Lorem ipsum dolor sit amet, consectetur adipiscing elit, sed do eiusmod tempor incididunt ut labore et dolore magna aliqua. Ut enim ad minim veniam, quis ostrud itation ullamco</p><div class="deal-badge"></div><div class="deal-text"><b>50%</b><small>OFF</small></div><div class="order-bar"><svg viewBox="0 0 12 12"><circle cx="6" cy="6" r="5.5" fill="#fff"/><path d="M4 3.2l1.1 1.5-.7.8c.5 1 1.2 1.7 2.1 2.1l.8-.7 1.5 1.1-.6 1c-2.6-.4-4.5-2.4-4.9-5z" fill="#1d1d1d"/></svg><span>ORDER NOW</span></div><i class="base-stripe"></i></article>
</main>

<aside class="info-panel">
  <div class="info-word">INFO</div>
  <div class="board-letters"><span>B</span><span>O</span><span>A</span><span>R</span><span>D</span></div>
</aside>

</body>
</html>
```